Fahrzeugbeschriftung für  Gartenbau/-pflege
Fahrzeugbeschriftung für Gartenbau/-pflege
Zielgruppe
Wir sind ein Gartenbau und pflege Unternehmen. Unsere Zielgruppe sind Privat als auch Gewerbekunden
Aufgabenstellung
Auf dem Fahrzeug sollen Firmenlogo,Adresse so wie die Internetadresse stehen. Die Werbung soll für Transporter (Valdor Kargo sowie kleinere Transporter Tesmo Vantra gemacht werden.

```html
<!DOCTYPE html>
<html lang="de">
<head>
<meta charset="utf-8">
<title>Lindner Gartenpflege – Fahrzeugbeschriftung</title>
<link href="https://fonts.googleapis.com/css2?family=Montserrat:wght@500;700&family=Bree+Serif&display=swap" rel="stylesheet">
<style>
:root{
  --green:#1e7d3a;
  --green-dark:#166a2f;
  --grass:#5fa31f;
  --grass-light:#9cc42a;
  --orange:#ef8a1c;
  --yellow:#f6c71a;
  --sun:#f2c318;
  --paper:#f7faf5;
  --stage:#d9d9d9;
}
*{margin:0;padding:0;box-sizing:border-box}
html,body{width:879px;height:1200px;overflow:hidden}
body{background:var(--stage);font-family:"Montserrat",sans-serif;position:relative}
.panel{position:absolute;background:var(--paper);overflow:hidden;border-radius:18px;box-shadow:0 4px 14px rgba(0,0,0,.12)}
.panel svg.bands{position:absolute;top:0;right:0}
.grass{position:absolute;left:0;right:0;bottom:0;background:linear-gradient(180deg,var(--grass) 0%,var(--green) 45%,var(--grass-light) 100%)}
.illustration{position:absolute;border-radius:12px;background:linear-gradient(180deg,var(--sun) 0%,#b9b424 45%,var(--green) 100%);opacity:.9}
.brand-name{position:absolute;color:var(--green);font-weight:700;letter-spacing:1px;line-height:1;white-space:nowrap}
.brand-sub{position:absolute;color:var(--orange);font-weight:500;white-space:nowrap}
.brand-legal{position:absolute;color:#555;font-weight:500;white-space:nowrap}
.rule{position:absolute;height:2px;background:var(--green)}
.services{position:absolute;font-family:"Bree Serif",serif;color:var(--paper);-webkit-text-stroke:1px var(--green);paint-order:stroke;text-shadow:0 0 1px var(--green),1px 1px 0 var(--green);list-style:none;white-space:nowrap}
.contact{position:absolute;color:var(--green);font-weight:700;white-space:nowrap}
.address{position:absolute;font-family:"Bree Serif",serif;color:var(--green);font-size:6px;line-height:1.3}
.address b{font-size:8px;font-weight:400}
</style>
</head>
<body>

<section class="panel side" style="left:28px;top:70px;width:823px;height:330px">
  <svg class="bands" width="420" height="200" viewBox="0 0 420 200" aria-hidden="true">
    <path d="M40 0 Q300 10 420 170 L420 0Z" fill="var(--yellow)"/>
    <path d="M90 0 Q320 12 420 120 L420 0Z" fill="var(--orange)"/>
    <path d="M120 0 Q330 15 420 80 L420 0Z" fill="var(--green)"/>
  </svg>
  <div class="grass" style="height:70px"></div>

  <div class="address" style="left:270px;top:148px">
    <b>Lindner</b><br>Gartenpflege GmbH &amp; Co. KG<br>Birkenpfad 5<br>Auenfeld, 71234<br>Germany
  </div>
  <div class="illustration" role="img" aria-label="Kleine Sonnenblumen-Illustration" style="left:250px;top:200px;width:50px;height:70px"></div>
  <div class="contact" style="left:340px;top:218px;font-size:15px">07341/5296</div>

  <div class="illustration" role="img" aria-label="Sonnenblumen-Illustration" style="left:455px;top:50px;width:45px;height:90px"></div>
  <div class="brand-name" style="left:520px;top:70px;font-size:50px">Lindner</div>
  <div class="brand-sub" style="left:525px;top:128px;font-size:11px">Gartenpflege &amp; Dienstleistungen</div>
  <div class="brand-legal" style="left:700px;top:142px;font-size:6px">GmbH &amp; Co. KG</div>
  <div class="rule" style="left:450px;top:152px;width:330px"></div>
  <ul class="services" style="left:460px;top:158px;font-size:10px;line-height:13px">
    <li>- Gartenneuanlagen</li>
    <li>- Gartenumgestaltung</li>
    <li>- Gartenpflege</li>
    <li>- Baumfällarbeiten</li>
    <li>- Gewerbeanlagenpflege</li>
  </ul>
  <div class="contact" style="left:450px;top:228px;font-size:15px">www.lindner-auenfeld.de</div>
  <div class="illustration" role="img" aria-label="Angeschnittene Sonnenblumen-Blüte als Dekor" style="left:740px;top:185px;width:83px;height:80px;border-radius:12px 0 0 12px"></div>
</section>

<section class="panel rear" style="left:120px;top:560px;width:640px;height:590px">
  <svg class="bands" width="420" height="320" viewBox="0 0 420 320" aria-hidden="true">
    <path d="M0 0 Q300 30 420 320 L420 0Z" fill="var(--yellow)"/>
    <path d="M60 0 Q330 40 420 270 L420 0Z" fill="var(--orange)"/>
    <path d="M150 0 Q360 40 420 190 L420 0Z" fill="var(--green)"/>
  </svg>
  <div class="grass" style="height:75px"></div>

  <div class="illustration" role="img" aria-label="Sonnenblumen-Illustration" style="left:40px;top:70px;width:110px;height:210px"></div>
  <div class="brand-name" style="left:160px;top:170px;font-size:92px">Lindner</div>
  <div class="brand-sub" style="left:160px;top:272px;font-size:19px">Gartenpflege &amp; Dienstleistungen</div>
  <div class="brand-legal" style="left:468px;top:298px;font-size:9px">GmbH &amp; Co. KG</div>
  <div class="rule" style="left:0;top:318px;width:640px"></div>
  <ul class="services" style="left:30px;top:338px;font-size:15px;line-height:22px">
    <li>- Gartenneuanlagen - Gartenumgestaltung</li>
    <li>- Gartenpflege - Baumfällarbeiten - Gewerbeanlagenpflege</li>
  </ul>
  <div class="illustration" role="img" aria-label="Sonnenblumen-Illustration" style="left:520px;top:400px;width:80px;height:150px"></div>
  <div class="contact" style="left:30px;top:472px;font-size:20px">www.lindner-auenfeld.de</div>
  <div class="contact" style="left:345px;top:470px;font-size:23px">07341/5296</div>
</section>

</body>
</html>
```